Broschüre für Baumanagement
Zielgruppe
Baumanagement
Wir liefern von der Planung, über die notwendigen Handwerksfirmen langjährige Partner, Bauleitung alle notwenidgen Partner
Wir betreuen seit jahren Kunden aus dem Immobilienwesen, Handel usw.
Ein Ansprechpartner vond er Planung bis zur Übergabe
Aufgabenstellung
DIN A4, 2 Seiten, Modern, Fakten, Gerne nur in schwarz und weiss halten

```html
<!DOCTYPE html>
<html lang="de">
<head>
<meta charset="utf-8">
<title>Korvan Group – Broschüre Baumanagement</title>
<link href="https://fonts.googleapis.com/css2?family=Montserrat:wght@500;600;700;800&display=swap" rel="stylesheet">
<style>
  :root {
    --ink: #0b0b0b;
    --paper: #ffffff;
    --stage: #d9d9d9;
    --mid-grey: #c9c9c9;
    --photo-light: #bdbdbd;
    --photo-dark: #4a4a4a;
    --text-soft: #e6e6e6;
  }
  * { box-sizing: border-box; margin: 0; padding: 0; }
  html, body { width: 906px; height: 1200px; overflow: hidden; }
  body {
    background: var(--stage);
    font-family: "Montserrat", Arial, sans-serif;
    position: relative;
  }
  .spread {
    position: absolute;
    top: 286px; left: 17px;
    display: flex; gap: 12px;
  }
  .page {
    position: relative;
    width: 430px; height: 627px;
    overflow: hidden;
    box-shadow: 0 10px 24px rgba(0,0,0,.35);
  }
  .page-shapes { position: absolute; inset: 0; }

  /* back page */
  .back { background: var(--ink); color: var(--paper); }
  .back-copy { position: absolute; left: 56px; top: 364px; width: 340px; }
  .service-title { font-size: 14px; font-weight: 700; margin-bottom: 4px; }
  .service-text { font-size: 10.5px; font-weight: 500; line-height: 1.5; color: var(--text-soft); }
  .service-claim { font-size: 10.5px; font-weight: 700; line-height: 1.5; margin-top: 6px; }
  .contact-label {
    position: absolute; left: 56px; top: 498px;
    color: var(--ink); font-size: 14px; font-weight: 700;
  }
  .contact-phone {
    position: absolute; left: 56px; top: 536px;
    display: flex; align-items: center; gap: 5px;
    font-size: 22px; font-weight: 700;
  }
  .contact-web { position: absolute; left: 56px; top: 567px; font-size: 15px; font-weight: 500; }

  /* front page */
  .front { background: var(--paper); color: var(--ink); }
  .brand {
    position: absolute; top: 72px; left: 0; right: 0;
    display: flex; flex-direction: column; align-items: center;
  }
  .brand-row { display: flex; align-items: center; gap: 10px; }
  .brand-mark { width: 16px; height: 16px; background: var(--ink); }
  .brand-name { font-size: 24px; font-weight: 800; letter-spacing: .5px; }
  .brand-sub { font-size: 7px; font-weight: 700; letter-spacing: 1.6px; margin-top: 4px; }
  .tagline-band {
    position: absolute; top: 150px; left: 45px; right: 0; height: 25px;
    background: var(--ink); color: var(--paper);
    font-size: 8.5px; font-weight: 600;
    display: flex; align-items: center; padding-left: 18px;
  }
  .headline {
    position: absolute; top: 193px; left: 0; right: 0;
    text-align: center; font-size: 15.5px; font-weight: 600; line-height: 1.32;
  }
  .headline strong { font-weight: 800; }
</style>
</head>
<body>
  <main class="spread">
    <section class="page back">
      <svg class="page-shapes" viewBox="0 0 430 627" aria-hidden="true">
        <defs>
          <linearGradient id="office-tone" x1="0" y1="0" x2="0" y2="1">
            <stop offset="0" stop-color="var(--photo-light)"/>
            <stop offset="1" stop-color="#7a7a7a"/>
          </linearGradient>
        </defs>
        <polygon points="0,0 430,0 430,318 0,335" fill="url(#office-tone)" role="img" aria-label="Foto: Besprechungsraum mit Glaswänden und Blick auf die Stadt"/>
        <polygon points="0,335 430,318 430,324 0,343" fill="var(--paper)"/>
        <polygon points="0,496 271,496 266,519 0,519" fill="var(--paper)"/>
        <circle cx="62" cy="551" r="7.5" fill="var(--paper)"/>
        <path d="M59 547 q-1 5 4 8 l2-2 -2-2 -1 1 q-2-1-2-3 l1-1 -2-2 z" fill="var(--ink)"/>
      </svg>
      <div class="back-copy">
        <h2 class="service-title">Baumanagement</h2>
        <p class="service-text">Wir liefern von der Planung, über die notwendigen Handwerksfirmen langjährige Partner, Bauleitung alle notwenidgen Partner</p>
        <p class="service-claim">Ein Ansprechpartner vond er Planung<br>bis zur Übergabe</p>
      </div>
      <p class="contact-label">Kontaktieren Sie uns</p>
      <p class="contact-phone"><span style="width:15px"></span>123-456-7890</p>
      <p class="contact-web">www.korvan-bau.de</p>
    </section>

    <section class="page front">
      <svg class="page-shapes" viewBox="0 0 430 627" aria-hidden="true">
        <defs>
          <linearGradient id="tower-tone" x1="0" y1="0" x2="0" y2="1">
            <stop offset="0" stop-color="#9a9a9a"/>
            <stop offset="1" stop-color="var(--photo-dark)"/>
          </linearGradient>
        </defs>
        <polygon points="0,268 430,290 0,300" fill="var(--mid-grey)"/>
        <polygon points="0,300 220,290 430,290 430,627 0,627" fill="url(#tower-tone)" role="img" aria-label="Foto: Blick von unten auf gläserne Hochhäuser"/>
      </svg>
      <div class="brand">
        <div class="brand-row">
          <span class="brand-mark"></span>
          <span class="brand-name">KORVAN GROUP</span>
        </div>
        <span class="brand-sub">REAL ESTATE INVESTMENT</span>
      </div>
      <p class="tagline-band">WE HAVE BEEN A REAL ESTATE CONSULTANCY FOR MANY YEARS.</p>
      <h1 class="headline">WE ADVISE AND MEDIATE PRIMARILY<br>IN THE COMMERCIAL AND<br><strong>RESIDENTIAL ASSET CLASSES.</strong></h1>
    </section>
  </main>
</body>
</html>
```